Bows Catalog Cover

Cover Page for a catalog for bows. Same logo MOR Morvane Alpina Cordaria.
Catalog overview: https://www.folioworks-demo.net/MOR-Morvane-Alpina-Cordaria/catalogs/MOR-catalog.html
No instruments, no scores, Only bows or bow parts (head, frog ...). Drawings or pictures.

Target Market(s)

Violin makers and reseller

Requirements
Must have
• bows or bow parts
Nice to have
• Drawings and or pictures
Should not have
• full Instruments or scores

```html
<!DOCTYPE html>
<html lang="fr">
<head>
<meta charset="utf-8">
<title>MOR – Archets 2021 – Couverture</title>
<link href="https://fonts.googleapis.com/css2?family=Montserrat:wght@600;700;800&display=swap" rel="stylesheet">
<style>
  :root {
    --page-bg: #c6c6c6;
    --cover-dark: #360f2e;
    --cover-mid: #4a0c3c;
    --cover-glow: #6b2a5e;
    --stripe: #4a0a3a;
    --frame: #ffffff;
    --title: #ebc1dc;
    --brand: #5b2c9c;
    --accent-red: #ff3b45;
    --photo-light: #f4f3f2;
    --photo-shade: #dcdad8;
  }
  * { box-sizing: border-box; margin: 0; padding: 0; }
  html, body {
    width: 1067px;
    height: 1200px;
    overflow: hidden;
    background: var(--page-bg);
  }
  .cover {
    position: absolute;
    left: 123px;
    top: 20px;
    width: 821px;
    height: 1160px;
    background: radial-gradient(ellipse 62% 48% at 51% 52%, var(--cover-glow) 0%, var(--cover-mid) 62%, var(--cover-dark) 100%);
    box-shadow: 0 6px 24px rgba(0,0,0,0.25);
    overflow: hidden;
  }
  .cover-art {
    position: absolute;
    inset: 0;
    width: 100%;
    height: 100%;
  }
  .brand-box {
    position: absolute;
    left: 291px;
    top: 44px;
    width: 228px;
    height: 80px;
    background: #fff;
    display: flex;
    align-items: center;
    justify-content: center;
    gap: 10px;
  }
  .brand-mark {
    width: 30px;
    height: 30px;
    border-radius: 50%;
    background: var(--brand);
  }
  .brand-text {
    display: flex;
    flex-direction: column;
    font-family: "Montserrat", sans-serif;
    font-weight: 800;
    color: var(--brand);
    line-height: 1;
  }
  .brand-name { font-size: 38px; letter-spacing: 2px; }
  .brand-tagline { font-size: 6.5px; letter-spacing: 0.6px; margin-top: 4px; }
  .cover-title {
    position: absolute;
    left: 0;
    right: 0;
    top: 994px;
    text-align: center;
    font-family: "Montserrat", sans-serif;
    font-weight: 700;
    font-size: 64px;
    color: var(--title);
    letter-spacing: 0.5px;
  }
</style>
</head>
<body>
  <main class="cover">
    <svg class="cover-art" viewBox="0 0 1127 1593" xmlns="http://www.w3.org/2000/svg">
      <defs>
        <linearGradient id="photoFill" x1="0" y1="0" x2="1" y2="1">
          <stop offset="0" stop-color="var(--photo-light)"/>
          <stop offset="0.5" stop-color="var(--photo-shade)"/>
          <stop offset="1" stop-color="var(--photo-light)"/>
        </linearGradient>
        <radialGradient id="sparkGlow">
          <stop offset="0" stop-color="#fff3c0"/>
          <stop offset="0.3" stop-color="var(--accent-red)" stop-opacity="0.9"/>
          <stop offset="1" stop-color="var(--accent-red)" stop-opacity="0"/>
        </radialGradient>
      </defs>

      <g class="top-stripes" fill="var(--stripe)">
        <rect x="128" y="0" width="50" height="101"/>
        <rect x="245" y="0" width="50" height="101"/>
        <rect x="359" y="0" width="51" height="101"/>
        <rect x="720" y="0" width="50" height="101"/>
        <rect x="836" y="0" width="50" height="101"/>
        <rect x="949" y="0" width="51" height="101"/>
      </g>

      <g class="frame" fill="none" stroke="var(--frame)" stroke-width="3">
        <line x1="400" y1="55" x2="598" y2="55"/>
        <line x1="515" y1="177" x2="713" y2="177"/>
        <line x1="121" y1="105" x2="400" y2="105"/>
        <line x1="713" y1="105" x2="1007" y2="105"/>
        <path d="M121 105 C150 140 150 220 50 232"/>
        <path d="M1007 105 C978 140 978 220 1076 232"/>
        <line x1="50" y1="232" x2="50" y2="710"/>
        <line x1="50" y1="912" x2="50" y2="1385"/>
        <line x1="1076" y1="232" x2="1076" y2="710"/>
        <line x1="1076" y1="912" x2="1076" y2="1385"/>
        <path d="M50 1385 C145 1395 150 1495 102 1535"/>
        <path d="M1076 1385 C983 1395 978 1495 1026 1535"/>
        <line x1="102" y1="1535" x2="463" y2="1535"/>
        <line x1="647" y1="1535" x2="1026" y2="1535"/>
      </g>
      <g class="frame-dots" fill="var(--frame)">
        <circle cx="121" cy="105" r="5"/>
        <circle cx="1007" cy="105" r="5"/>
        <circle cx="50" cy="232" r="5"/>
        <circle cx="1076" cy="232" r="5"/>
        <circle cx="50" cy="807" r="5"/>
        <circle cx="1076" cy="807" r="5"/>
        <circle cx="50" cy="1385" r="5"/>
        <circle cx="1076" cy="1385" r="5"/>
        <circle cx="102" cy="1535" r="5"/>
        <circle cx="1026" cy="1535" r="5"/>
        <circle cx="560" cy="1535" r="5"/>
      </g>

      <g class="light-trails" fill="none" stroke="var(--accent-red)" stroke-linecap="round">
        <path d="M870 373 Q985 335 1020 440 Q1030 500 920 512" stroke-width="4" opacity="0.9"/>
        <path d="M262 1058 Q250 1160 415 1226" stroke-width="4" opacity="0.9"/>
        <circle cx="937" cy="369" r="22" fill="url(#sparkGlow)" stroke="none"/>
        <circle cx="270" cy="1100" r="24" fill="url(#sparkGlow)" stroke="none"/>
      </g>

      <circle class="medallion-ring" cx="577" cy="778" r="402" fill="none" stroke="var(--frame)" stroke-width="16"/>
      <circle class="medallion-photo" cx="577" cy="778" r="378" fill="url(#photoFill)" role="img" aria-label="Photograph of a hand holding a violin bow, overlaid with a drawing of a bow with its head and frog"/>
    </svg>

    <div class="brand-box">
      <span class="brand-mark"></span>
      <div class="brand-text">
        <span class="brand-name">MOR</span>
        <span class="brand-tagline">MORVANE ALPINA CORDARIA</span>
      </div>
    </div>

    <h1 class="cover-title">ARCHETS - 2021</h1>
  </main>
</body>
</html>
```